Residential & commercial landscaping company

Updated business cards for commercial and landscaping company. We would like to keep out logo, but just need a more updated business card.

```html
<!DOCTYPE html>
<html lang="en">
<head>
<meta charset="utf-8">
<title>Fernvale Business Cards</title>
<link href="https://fonts.googleapis.com/css2?family=Arimo:wght@400;700&display=swap" rel="stylesheet">
<style>
  :root {
    --backdrop: #c4c4c4;
    --card-green: #5b8139;
    --accent-green: #7cc142;
    --paper: #ffffff;
    --ink: #1a1a1a;
  }
  html, body {
    margin: 0;
    padding: 0;
    width: 1200px;
    height: 788px;
    overflow: hidden;
    background: var(--backdrop);
    font-family: "Arimo", Arial, sans-serif;
  }
  .stage {
    position: relative;
    width: 1200px;
    height: 788px;
  }
  .card {
    position: absolute;
    top: 245px;
    width: 520px;
    height: 297px;
    border-radius: 20px;
    overflow: hidden;
    box-shadow: 0 8px 24px rgba(0,0,0,0.25);
  }
  .card--front { left: 60px; background: var(--paper); }
  .card--back { left: 620px; background: var(--card-green); }

  .front-wave {
    position: absolute;
    inset: 0;
    width: 100%;
    height: 100%;
  }
  .wave-fill { fill: var(--card-green); }
  .wave-stripe { fill: var(--accent-green); }

  .brand {
    position: absolute;
    display: flex;
    align-items: center;
    gap: 12px;
    font-weight: 700;
    line-height: 1;
  }
  .brand__mark {
    background: var(--accent-green);
  }
  .card--front .brand {
    top: 32px;
    left: 180px;
    color: var(--ink);
    font-size: 36px;
  }
  .card--front .brand__mark { width: 30px; height: 30px; }

  .card--back .brand {
    top: 50%;
    left: 50%;
    transform: translate(-50%, -50%);
    color: var(--paper);
    font-size: 60px;
  }
  .card--back .brand__mark { width: 50px; height: 50px; }

  .contact {
    position: absolute;
    left: 34px;
    bottom: 22px;
    color: var(--paper);
  }
  .contact__name {
    margin: 0;
    font-size: 21px;
    font-weight: 700;
  }
  .contact__role {
    margin: 3px 0 12px;
    font-size: 13px;
  }
  .contact__list {
    list-style: none;
    margin: 0;
    padding: 0;
    font-size: 13px;
    line-height: 1.55;
  }
  .contact__list li {
    display: flex;
    align-items: center;
    gap: 7px;
  }
  .contact__icon {
    width: 11px;
    height: 11px;
    fill: var(--paper);
    flex: none;
  }
</style>
</head>
<body>
<main class="stage">

  <section class="card card--front" aria-label="Business card front">
    <svg class="front-wave" viewBox="0 0 520 297" preserveAspectRatio="none" aria-hidden="true">
      <path class="wave-stripe" d="M0,126 C160,98 300,114 400,74 C460,48 490,26 520,26 L520,40 C490,40 460,62 400,88 C300,128 160,112 0,140 Z"/>
      <path class="wave-fill" d="M0,140 C160,112 300,128 400,88 C460,62 490,40 520,40 L520,297 L0,297 Z"/>
    </svg>

    <div class="brand">
      <span class="brand__mark"></span>
      <span class="brand__name">Fernvale</span>
    </div>

    <div class="contact">
      <h2 class="contact__name">Daniel Porter Jr.</h2>
      <p class="contact__role">Project Manager</p>
      <ul class="contact__list">
        <li>
          <svg class="contact__icon" viewBox="0 0 24 24" aria-hidden="true"><path d="M6.6 10.8a15.1 15.1 0 0 0 6.6 6.6l2.2-2.2c.3-.3.7-.4 1-.2 1.1.4 2.3.6 3.6.6.6 0 1 .4 1 1V20c0 .6-.4 1-1 1C10.6 21 3 13.4 3 4c0-.6.4-1 1-1h3.5c.6 0 1 .4 1 1 0 1.3.2 2.5.6 3.6.1.3 0 .7-.2 1z"/></svg>
          555-214-0380 ext. 412
        </li>
        <li>
          <svg class="contact__icon" viewBox="0 0 24 24" aria-hidden="true"><path d="M6 2h12v5H6zM4 8h16a2 2 0 0 1 2 2v7h-4v5H6v-5H2v-7a2 2 0 0 1 2-2zm4 8v4h8v-4z"/></svg>
          555-736-9028
        </li>
        <li>
          <svg class="contact__icon" viewBox="0 0 24 24" aria-hidden="true"><path d="M2 5h20v14H2zm2 2v.5l8 5 8-5V7z"/></svg>
          dan@fernvalelandscape.com
        </li>
      </ul>
    </div>
  </section>

  <section class="card card--back" aria-label="Business card back">
    <div class="brand">
      <span class="brand__mark"></span>
      <span class="brand__name">Fernvale</span>
    </div>
  </section>

</main>
</body>
</html>
```